Letterhead - Quarrington Law Group

I receive a fantastic logo from you guys and I'd like to incorporate it into business cards and letterhead. I accidentally approved design No. 32361474 and contacted designer Ravindra, and Ravindra sent me the zip folder for Design No. 32361417, which I very much appreciate.
I'd like to order business cards and letterhead with Design No. 32361417 as soon as possible, but I want to make sure that you incorporate the correct design (attached). I'd also like to provide my information to add (address, phone number, email, fax) but I'm not quite sure how to do it.
The information that I would like on the business cards and letterhead is as follows:
Quarrington Law Group
Theodore K. Quarrington, Esq.
2741 Hollis Avenue, Suite 520
San Francisco, CA 94087
Office: (415) 378-6130
Fax: (415) 746-0183
ted@quarringtonlawgroup-example.com
Thanks in advance for any guidance.
Ted Quarrington
Quarrington Law Group
(415) 831-4497 (cell)

```html
<!DOCTYPE html>
<html lang="en">
<head>
<meta charset="utf-8">
<title>Quarrington Law Group – Letterhead</title>
<link rel="stylesheet" href="https://fonts.googleapis.com/css2?family=Arimo:wght@400;700&family=Allura&display=swap">
<style>
  :root {
    --backdrop: #e9eaec;
    --paper: #ffffff;
    --ink: #2b2b2b;
    --ink-soft: #3a3a3a;
    --brand-blue: #1a8fd0;
    --band-black: #1e1e1e;
    --on-blue: #ffffff;
  }
  * { box-sizing: border-box; margin: 0; padding: 0; }
  html, body {
    width: 1200px; height: 874px; overflow: hidden;
    background: var(--backdrop);
    font-family: "Arimo", Arial, sans-serif;
  }
  .letterhead {
    position: absolute; left: 310px; top: 27px;
    width: 580px; height: 820px;
    background: var(--paper);
    box-shadow: 0 2px 10px rgba(0,0,0,0.12);
    overflow: hidden;
    color: var(--ink);
  }
  .firm-mark {
    position: absolute; left: 52px; top: 108px;
    display: flex; align-items: center; gap: 10px;
  }
  .firm-mark__square {
    width: 18px; height: 18px; background: var(--brand-blue);
  }
  .firm-mark__name {
    font-size: 21px; font-weight: 700; color: var(--band-black);
    letter-spacing: 0.5px;
  }
  .contact-block {
    position: absolute; left: 330px; top: 48px;
    padding-left: 14px;
    border-left: 1px solid var(--brand-blue);
    font-size: 9.5px; line-height: 13px; color: var(--ink-soft);
  }
  .contact-block__firm { color: var(--brand-blue); font-weight: 700; font-size: 10.5px; }
  .contact-line { display: flex; align-items: center; gap: 5px; }
  .contact-line svg { width: 8px; height: 8px; fill: var(--brand-blue); }
  .letter-body {
    position: absolute; left: 80px; top: 215px; width: 440px;
    font-size: 9.6px; line-height: 13.2px; color: var(--ink);
  }
  .letter-body p { margin-bottom: 14px; }
  .letter-body .salutation { margin-bottom: 6px; }
  .sign-off { margin-top: 6px; margin-bottom: 0 !important; }
  .signature {
    font-family: "Allura", cursive;
    color: var(--brand-blue);
    font-size: 34px; line-height: 36px; margin-top: 2px;
  }
  .footer-wave { position: absolute; left: 0; bottom: 0; width: 580px; height: 820px; }
  .footer-card {
    position: absolute; right: 26px; top: 560px; width: 190px;
    color: var(--on-blue); text-align: left;
    font-size: 9.5px; line-height: 13px;
  }
  .footer-card__name { font-weight: 700; font-size: 13px; line-height: 17px; }
  .footer-card .contact-line svg { fill: var(--on-blue); }
</style>
</head>
<body>
<main class="letterhead">
  <svg class="footer-wave" viewBox="0 0 580 820" aria-hidden="true">
    <path d="M232 820 C 400 790, 450 640, 505 545 C 530 505, 555 478, 580 470 L 580 478 C 560 484, 538 510, 514 550 C 460 645, 410 800, 252 820 Z" fill="var(--band-black)"/>
    <path d="M252 820 C 410 800, 460 645, 514 550 C 538 510, 560 484, 580 478 L 580 820 Z" fill="var(--brand-blue)"/>
  </svg>

  <div class="firm-mark">
    <span class="firm-mark__square"></span>
    <span class="firm-mark__name">Quarrington Law Group</span>
  </div>

  <address class="contact-block">
    <div class="contact-block__firm">Quarrington Law Group</div>
    <div>Theodore K. Quarrington, Esq.</div>
    <div>2741 Hollis Avenue, Suite 520</div>
    <div>San Francisco, CA 94087</div>
    <div class="contact-line"><svg viewBox="0 0 10 10"><path d="M2 0 L4 2 L3 3.5 Q4.5 6 6.5 7 L8 6 L10 8 L8.5 10 Q3 9 0 1.5 Z"/></svg>(415) 378-6130</div>
    <div class="contact-line"><svg viewBox="0 0 10 10"><rect x="2" y="0" width="6" height="3"/><rect x="0" y="3.5" width="10" height="4"/><rect x="2" y="8" width="6" height="2"/></svg>(415) 746-0183</div>
    <div class="contact-line"><svg viewBox="0 0 10 10"><path d="M0 2 H10 V8 H0 Z M0 2 L5 6 L10 2" stroke="#fff" stroke-width="0.8"/></svg>ted@quarringtonlawgroup-example.com</div>
  </address>

  <article class="letter-body">
    <p class="salutation">Dear Sir,</p>
    <p>Lorem ipsum dolor sit amet, consectetur adipiscing elit, sed do eiusmod tempor incididunt ut labore et dolore magna aliqua. Ut enim ad minim veniam, quis nostrud exercitation ullamco laboris nisi ut aliquip ex ea commodo consequat. Duis aute irure dolor in reprehenderit in voluptate velit esse cillum dolore eu fugiat nulla pariatur. Excepteur sint occaecat cupidatat non proident, sunt in culpa qui officia deserunt mollit anim id est laborum. It is a long established fact that a reader will be distracted by the readable content of a page when looking at its layout. The point of using Lorem Ipsum is that it has a more-or-less normal distribution of letters, as opposed to using ‘Content here, content here’, making it look like readable English.</p>
    <p>But I must explain to you how all this mistaken idea of denouncing pleasure and praising pain was born and I will give you a complete account of the system, and expound the actual teachings of the great explorer of the truth, the master-builder of human happiness. No one rejects, dislikes, or avoids pleasure itself, because it is pleasure, but because those who do not know how to pursue pleasure rationally encounter consequences that are extremely painful. Nor again is there anyone who loves or pursues or desires to obtain pain of itself, because it is pain, but because occasionally circumstances occur in which toil and pain can procure him some great pleasure.</p>
    <p>There are many variations of passages of Lorem Ipsum available, but the majority have suffered alteration in some form, by injected humour, or randomised words which don’t look even slightly believable. If you are going to use a passage of Lorem Ipsum, you need to be sure there isn’t anything embarrassing hidden in the middle of text. All the Lorem Ipsum generators on the Internet tend to repeat predefined chunks as necessary, making this the first true generator on the Internet.</p>
    <p class="sign-off">Best Regards</p>
    <div class="signature">Martin Ellery</div>
  </article>

  <div class="footer-card">
    <div class="footer-card__name">Ted Quarrington</div>
    <div>Quarrington Law Group</div>
    <div class="contact-line"><svg viewBox="0 0 10 10"><path d="M2 0 L4 2 L3 3.5 Q4.5 6 6.5 7 L8 6 L10 8 L8.5 10 Q3 9 0 1.5 Z"/></svg>(415) 831-4497 (cell)</div>
  </div>
</main>
</body>
</html>
```